Halvex Consulting

Hi,
I have my own network consulting business (just me)
and need to get a logo and business card design together,

Based in New Zealand,

Gareth Pollard
Unified Communications and Network Architect

/design engineer,
and would like this to be the basis for personal branding and company identity

Reason: I will be off site for a couple of days - so you have some more time

Business

• I have the basis for a optional logo - needs color -

```html
<!DOCTYPE html>
<html lang="en">
<head>
<meta charset="utf-8">
<title>Halvex Consulting – Business Card</title>
<link rel="stylesheet" href="https://fonts.googleapis.com/css2?family=Open+Sans:wght@400;700&display=swap">
<style>
  :root {
    --backdrop-top: #c9cacc;
    --backdrop-bottom: #eceded;
    --card: #ffffff;
    --ink: #1f1f1f;
    --brand-pink: #e94f7c;
    --brand-magenta: #e0307f;
    --brand-yellow: #ffc94d;
    --divider: #2b2b2b;
  }
  * { margin: 0; padding: 0; box-sizing: border-box; }
  html, body { width: 1200px; height: 822px; overflow: hidden; }
  body {
    background: linear-gradient(180deg, var(--backdrop-top), var(--backdrop-bottom));
    font-family: "Open Sans", Arial, sans-serif;
    color: var(--ink);
    position: relative;
  }
  .card {
    position: absolute;
    left: 164px; top: 169px;
    width: 874px; height: 484px;
    background: var(--card);
    overflow: hidden;
  }
  .decor-glow {
    position: absolute;
    left: 360px; top: 20px;
    width: 600px; height: 560px;
  }
  .brand-mark {
    position: absolute;
    left: 47px; top: 40px;
    width: 64px; height: 64px;
    border-radius: 50%;
    background: var(--brand-magenta);
  }
  .brand-name {
    position: absolute;
    left: 126px; top: 130px;
    font-size: 27px;
    font-weight: 700;
    color: var(--brand-pink);
    letter-spacing: 0.5px;
    text-transform: uppercase;
  }
  .person {
    position: absolute;
    left: 126px; top: 252px;
  }
  .person-name {
    font-size: 40px;
    font-weight: 400;
    line-height: 1.1;
    margin-bottom: 8px;
  }
  .person-role {
    font-size: 20px;
    line-height: 29px;
  }
  .divider {
    position: absolute;
    left: 484px; top: 263px;
    width: 3px; height: 148px;
    background: var(--divider);
  }
  .contact {
    position: absolute;
    left: 508px; top: 262px;
    list-style: none;
    font-size: 20px;
    line-height: 29px;
  }
  .contact li {
    display: flex;
    align-items: flex-start;
  }
  .contact-icon {
    width: 24px; height: 29px;
    margin-right: 14px;
    flex: none;
    display: flex; align-items: center; justify-content: center;
    font-weight: 700;
    font-size: 22px;
  }
  .contact-icon svg { width: 22px; height: 22px; fill: var(--ink); }
</style>
</head>
<body>
  <section class="card">
    <svg class="decor-glow" viewBox="0 0 600 560" role="img" aria-label="Large faint brand decoration in soft yellow to pink">
      <defs>
        <linearGradient id="glowFill" x1="0" y1="0" x2="0" y2="1">
          <stop offset="0" stop-color="var(--brand-yellow)" stop-opacity="0.35"/>
          <stop offset="1" stop-color="var(--brand-magenta)" stop-opacity="0.3"/>
        </linearGradient>
      </defs>
      <circle cx="260" cy="280" r="250" fill="url(#glowFill)"/>
    </svg>

    <div class="brand-mark"></div>
    <div class="brand-name">Halvex Consulting</div>

    <div class="person">
      <h1 class="person-name">Gareth Pollard</h1>
      <p class="person-role">Unified Communications<br>and Network Architect<br>Design engineer</p>
    </div>

    <div class="divider"></div>

    <ul class="contact">
      <li>
        <span class="contact-icon"><svg viewBox="0 0 24 24"><path d="M2 5h20v14H2z M3.5 6.5 12 13l8.5-6.5v-.5h-17z" fill-rule="evenodd"/></svg></span>
        <span>42 Harbour View Rd,<br>New Zealand</span>
      </li>
      <li>
        <span class="contact-icon"><svg viewBox="0 0 24 24"><path d="M2 9c0-3 4-5 10-5s10 2 10 5v2h-5V8.5c-1.5-.6-3.2-.9-5-.9s-3.5.3-5 .9V11H2z M5 13h14l2 7H3z"/></svg></span>
        <span>021 555 0142</span>
      </li>
      <li>
        <span class="contact-icon"><svg viewBox="0 0 24 24"><path d="M6 2h10l2 2v5H6z M3 10h18v8h-3v4H6v-4H3z M8 15v5h8v-5z"/></svg></span>
        <span>09 555 0178</span>
      </li>
      <li>
        <span class="contact-icon">@</span>
        <span>hello@halvex.co.nz</span>
      </li>
    </ul>
  </section>
</body>
</html>
```